KVT Business Cards

We require business cards for our business. We would like a matte black back to the card, with our logo centred in the middle. The front side of the card is open to design.

Target Market(s)

Clients looking for legal services (professional)

Industry/Entity Type

Legal

Contact Information for Business Card

Boris Telemark
Partner
Mobile: 0438 715 642
Email: boris@kvtlaw.co
Website: www.kvtlaw.co
Level 3, 118 Wexbury Street
Sydney NSW 2000

Font styles to use
Other font styles liked:
• Avenir

Colors
f04a50
ffffff
1b1b1b

Requirements
Must have
• Black back with logo included in the centre of the card.
• Our font is Avenir.

```html
<!DOCTYPE html>
<html lang="en">
<head>
<meta charset="utf-8">
<title>KVT Business Cards</title>
<link rel="stylesheet" href="https://fonts.googleapis.com/css2?family=Fira+Sans:wght@400;500;700&display=swap">
<style>
  :root {
    --stage: #3b3b3b;
    --stage-edge: #262626;
    --ink: #111111;
    --card-black: #141414;
    --paper: #ffffff;
    --red-deep: #b81d45;
    --red-bright: #dc2a52;
    --text-light: #ffffff;
    --text-soft: #e8e8e8;
  }
  * { box-sizing: border-box; margin: 0; padding: 0; }
  html, body {
    width: 1200px; height: 900px; overflow: hidden;
  }
  body {
    background: radial-gradient(ellipse at 50% 40%, var(--stage) 0%, var(--stage-edge) 100%);
    font-family: "Fira Sans", Arial, sans-serif;
    position: relative;
  }
  .card {
    position: absolute;
    left: 290px;
    width: 620px;
    height: 354px;
    overflow: hidden;
    box-shadow: 0 14px 30px rgba(0,0,0,0.55);
  }
  .card-back { top: 62px; background: var(--card-black); }
  .card-front { top: 476px; background: var(--card-black); }

  /* Back */
  .back-texture {
    position: absolute; inset: 0;
    background: radial-gradient(ellipse at 45% 70%, #2c2c2c 0%, #161616 55%, #0c0c0c 100%);
  }
  .back-brand {
    position: absolute; top: 50%; left: 50%;
    transform: translate(-50%, -50%);
    display: flex; align-items: center; gap: 26px;
  }
  .brand-square {
    width: 70px; height: 70px; background: var(--paper);
  }
  .brand-name {
    color: var(--text-light);
    font-weight: 700;
    font-size: 34px;
    line-height: 1.02;
    letter-spacing: 0.5px;
    text-transform: uppercase;
  }

  /* Front */
  .front-shapes { position: absolute; inset: 0; }
  .name-block {
    position: absolute; left: 0; top: 22px;
    display: flex; gap: 20px;
  }
  .name-tab { width: 20px; height: 40px; background: var(--paper); }
  .person-name {
    color: var(--text-light);
    font-weight: 700;
    font-size: 24px;
    letter-spacing: 0.6px;
    text-transform: uppercase;
    line-height: 1;
    margin-top: 2px;
  }
  .person-role {
    color: var(--text-soft);
    font-size: 15px;
    margin-top: 5px;
  }
  .contact-list {
    position: absolute; left: 40px; top: 170px;
    list-style: none;
    color: var(--text-light);
    font-size: 17px;
  }
  .contact-list li {
    display: flex; align-items: center; gap: 12px; height: 25px;
  }
  .contact-icon { width: 17px; height: 17px; fill: var(--text-light); }
  .address {
    position: absolute; left: 40px; top: 268px;
    color: var(--text-light);
    font-size: 18px;
    line-height: 1.3;
    font-style: normal;
  }
</style>
</head>
<body>

<section class="card card-back" aria-label="Card back">
  <div class="back-texture" role="img" aria-label="Fine diagonal square texture on matte black"></div>
  <div class="back-brand">
    <div class="brand-square"></div>
    <div class="brand-name">Kovar<br>Telemark<br>Legal</div>
  </div>
</section>

<section class="card card-front" aria-label="Card front">
  <svg class="front-shapes" viewBox="0 0 620 354" preserveAspectRatio="none" aria-hidden="true">
    <defs>
      <linearGradient id="redBand" x1="0" y1="0" x2="1" y2="0">
        <stop offset="0" stop-color="var(--red-deep)"/>
        <stop offset="1" stop-color="var(--red-bright)"/>
      </linearGradient>
    </defs>
    <polygon points="0,0 390,0 320,132 0,132" fill="url(#redBand)"/>
    <polygon points="390,0 620,0 620,354 460,354 320,132" fill="var(--paper)"/>
  </svg>

  <div class="name-block">
    <div class="name-tab"></div>
    <div>
      <div class="person-name">Boris Telemark</div>
      <div class="person-role">Partner</div>
    </div>
  </div>

  <ul class="contact-list">
    <li>
      <svg class="contact-icon" viewBox="0 0 24 24" aria-hidden="true"><path d="M6.6 10.8a15.1 15.1 0 0 0 6.6 6.6l2.2-2.2c.3-.3.7-.4 1-.2 1.1.4 2.3.6 3.6.6.6 0 1 .4 1 1V20c0 .6-.4 1-1 1C10.6 21 3 13.4 3 4c0-.6.4-1 1-1h3.5c.6 0 1 .4 1 1 0 1.2.2 2.4.6 3.6.1.3 0 .7-.2 1L6.6 10.8z"/></svg>
      <span>0438 715 642</span>
    </li>
    <li>
      <svg class="contact-icon" viewBox="0 0 24 24" aria-hidden="true"><path d="M2 5h20v14H2V5zm2 2v.4l8 5.2 8-5.2V7H4zm16 2.8-8 5.2-8-5.2V17h16V9.8z"/></svg>
      <span>boris@kvtlaw.co</span>
    </li>
    <li>
      <svg class="contact-icon" viewBox="0 0 24 24" aria-hidden="true"><path d="M12 2a10 10 0 1 0 0 20 10 10 0 0 0 0-20zm0 2c1 0 2.2 1.9 2.7 5H9.3C9.8 5.9 11 4 12 4zm-4.6 1.4A13 13 0 0 0 7.3 9H4.8a8 8 0 0 1 2.6-3.6zM4.2 11h3c-.1.7-.1 1.3-.1 2h-3a8 8 0 0 1 .1-2zm.6 4h2.5c.2 1.3.5 2.5 1 3.5A8 8 0 0 1 4.8 15zM9.3 15h5.4c-.5 3.1-1.7 5-2.7 5s-2.2-1.9-2.7-5zm0-2c0-.7 0-1.3.1-2h5.2c.1.7.1 1.3.1 2H9.3zm7.4 2h2.5a8 8 0 0 1-3.5 3.5c.5-1 .8-2.2 1-3.5zm.1-2c0-.7 0-1.3-.1-2h3a8 8 0 0 1 .1 2h-3zm-.1-4a13 13 0 0 0-1-3.6A8 8 0 0 1 19.2 9h-2.5z"/></svg>
      <span>www.kvtlaw.co</span>
    </li>
  </ul>

  <address class="address">Level 3, 118 Wexbury Street<br>Sydney NSW 2000</address>
</section>

</body>
</html>
```